Business Card for New Business

Please design a business card using our logo and font files. This is only one card for one person, as listed in details section.

Industry/Entity Type

Business

Contact Information for Business Card

Carl Voserby

Phone 240.318.6624
Cell 703.581.4096
Email carl@moltravex.com

www.moltravex.com

Address
18250 Brennick Lane #314
Damascus, MD 20715

Font styles to use
Sans Serif

Requirements
Must have
• Information listed in detail section. Must be standard card size.

```html
<!DOCTYPE html>
<html lang="en">
<head>
<meta charset="utf-8">
<title>Moltravex Business Card</title>
<link href="https://fonts.googleapis.com/css2?family=Questrial&display=swap" rel="stylesheet">
<style>
  :root {
    --backdrop: #3a3a3c;
    --card: #050505;
    --brand-red: #d8412a;
    --brand-orange: #e0532b;
    --text-white: #f4f4f4;
    --rule-grey: #8a8a8a;
  }
  * { margin: 0; padding: 0; box-sizing: border-box; }
  html, body {
    width: 1200px; height: 900px; overflow: hidden;
    background: var(--backdrop);
    font-family: "Questrial", sans-serif;
  }
  .card {
    position: absolute;
    width: 560px; height: 320px;
    background: var(--card);
    box-shadow: 0 10px 24px rgba(0,0,0,0.45);
  }
  .card-front { left: 580px; top: 100px; }
  .card-back  { left: 60px;  top: 480px; }

  .brand {
    display: flex; align-items: center; gap: 10px;
    color: var(--brand-orange);
    line-height: 1;
  }
  .brand-dot {
    border-radius: 50%;
    background: var(--brand-red);
    flex: none;
  }
  .card-front .brand {
    position: absolute; left: 0; right: 0; top: 100px;
    justify-content: center; font-size: 68px;
  }
  .card-front .brand-dot { width: 44px; height: 44px; }
  .front-url {
    position: absolute; left: 0; right: 0; bottom: 40px;
    text-align: center; color: var(--text-white);
    font-size: 17px; letter-spacing: 1.5px;
  }

  .card-back .brand {
    position: absolute; left: 36px; top: 100px; font-size: 42px;
  }
  .card-back .brand-dot { width: 28px; height: 28px; }
  .divider {
    position: absolute; left: 272px; top: 60px;
    width: 1px; height: 200px; background: var(--rule-grey);
  }
  .contact {
    position: absolute; left: 300px; top: 74px;
    color: var(--text-white); font-size: 16px; line-height: 1.35;
  }
  .contact-name {
    color: var(--brand-red); font-size: 22px; margin-bottom: 10px;
  }
  .contact-address { margin-bottom: 10px; }
  .contact-list { list-style: none; }
  .contact-list li { display: flex; align-items: center; gap: 9px; }
  .contact-icon { width: 13px; height: 13px; flex: none; fill: var(--brand-red); }
</style>
</head>
<body>
  <section class="card card-front">
    <div class="brand"><span class="brand-dot"></span><span class="brand-name">moltravex</span></div>
    <p class="front-url">www.moltravex.com</p>
  </section>

  <section class="card card-back">
    <div class="brand"><span class="brand-dot"></span><span class="brand-name">moltravex</span></div>
    <div class="divider"></div>
    <div class="contact">
      <p class="contact-name">Carl Voserby</p>
      <p class="contact-address">18250 Brennick Lane #314<br>Damascus, MD 20715</p>
      <ul class="contact-list">
        <li>
          <svg class="contact-icon" viewBox="0 0 16 16"><path d="M3 1l3 3-1.6 2.2a9 9 0 0 0 5.4 5.4L12 10l3 3-2 2C6.5 15 1 9.5 1 3z"/></svg>
          240.318.6624
        </li>
        <li>
          <svg class="contact-icon" viewBox="0 0 16 16"><rect x="4" y="1" width="8" height="14" rx="1.5"/><rect x="5.5" y="3" width="5" height="8" fill="#050505"/></svg>
          703.581.4096
        </li>
        <li>
          <svg class="contact-icon" viewBox="0 0 16 16"><rect x="1" y="3" width="14" height="10"/><path d="M1 3l7 6 7-6" fill="none" stroke="#050505" stroke-width="1.4"/></svg>
          carl@moltravex.com
        </li>
        <li>
          <svg class="contact-icon" viewBox="0 0 16 16"><circle cx="8" cy="8" r="7"/><path d="M1 8h14M8 1c-3 3.5-3 10.5 0 14M8 1c3 3.5 3 10.5 0 14" fill="none" stroke="#050505" stroke-width="1"/></svg>
          www.moltravex.com
        </li>
      </ul>
    </div>
  </section>
</body>
</html>
```